Car Club Website- Ravelin Motor Guild of New Zealand

We have been running a website in NZ for Ravelin Car enthusiasts. The design was fairly basic and is in serious need of a revamp, http://quorbatelix.example.net/index.html. We are looking for a dynamic design that will be visually attractive ( and obvious ) to our visitors and incorporates the fundamentals of the previous website. The inmportant tabs are the forum, gallery and events and the website needs to be easy to use for everyone.

This is all about the cars and the people. Visually, you need to recognise that we are a NZ Car Club and as such we do not want graphics of Left Hand Drive Cars or anything obviously NOT from NZ.
Thanks, cheers Wes

I AM VERY INTERESTED TO SEE SOMETHING THAT IS TOTALLY DIFFERENT TO ANYTHING YET POSTED. THE DESIGNS WE HAVE ARE GOOD AND I WILL PICK ONE OF THOSE BUT REALLY WANT TO SEE SOMETHING CREATIVE AND EYE CATCHING. I HAVE NOW CHANGED TO NON REFUNDABLE SO SOMEONE WILL GET PAID.
Updates

HI All, thanks for input so far but I have not seen a really creative left field approach yet which I am looking for. Thanks, cheers Wes

Target Market(s)

Car Enthusiasts

Industry/Entity Type

Events

Requirements
Must have
• as per link website
Should not have
• Any obvious graphics not from NZ

```html
<!DOCTYPE html>
<html lang="en">
<head>
<meta charset="utf-8">
<title>Ravelin Guild of New Zealand</title>
<link href="https://fonts.googleapis.com/css2?family=Questrial&family=Open+Sans:wght@400;600&display=swap" rel="stylesheet">
<style>
:root{
  --ink:#2e2c2b;
  --paper:#f1f0eb;
  --white:#ffffff;
  --hero:#2a2624;
  --hero-edge:#4a4645;
  --panel:#1f1d1d;
  --black:#050505;
  --btn-dark:#2b2929;
  --muted:#b9b9b9;
  --banner:#c9c7c5;
  --banner-ink:#3a1010;
}
*{margin:0;padding:0;box-sizing:border-box}
html,body{width:993px;height:1200px;overflow:hidden}
body{position:relative;background:var(--paper);color:var(--ink);font-family:"Open Sans",sans-serif}
.abs{position:absolute}
.head-font{font-family:"Questrial",sans-serif}

.site-header{left:0;top:0;width:993px;height:123px;background:var(--white)}
.brand{left:101px;top:22px;font-family:"Questrial",sans-serif;color:var(--ink);line-height:1}
.brand .name{font-size:44px;display:block}
.brand .region{font-size:32px;display:block;margin-top:2px}
.social{left:770px;top:21px;display:flex;gap:13px}
.social span{width:28px;height:28px;border-radius:50%;background:#c4c4c4;display:block}
.top-nav{left:700px;top:102px;display:flex;gap:17px;font-family:"Questrial",sans-serif;font-size:12.5px;letter-spacing:.3px}

.hero{left:0;top:123px;width:993px;height:263px;background:var(--hero);border-bottom:5px solid var(--hero-edge)}
.hero-photo{left:102px;top:0;width:512px;height:263px;background:linear-gradient(180deg,#d8cfc4 0%,#b7a894 45%,#5d6a83 60%,#9a938b 100%)}
.hero-title{left:626px;top:60px;font-size:23px;color:var(--white)}
.hero-text{left:631px;top:102px;width:250px;font-size:13.2px;line-height:15px;color:var(--white)}
.btn{display:flex;height:30px}
.btn .label{background:var(--white);color:var(--ink);font-weight:600;font-size:13px;display:flex;align-items:center;justify-content:center}
.btn .arrow{background:var(--black);color:var(--white);display:flex;align-items:center;justify-content:center;font-weight:600;font-size:15px}
.hero-btn{left:634px;top:182px}
.hero-btn .label{width:98px}.hero-btn .arrow{width:37px;background:#1b1919}

.slider-dots{left:457px;top:394px;display:flex;gap:7px}
.slider-dots span{width:11px;height:11px;border-radius:50%;background:#222}
.slider-dots span.on{background:#ddd;border:2px solid #444}

.side-nav{left:103px;top:440px;font-family:"Questrial",sans-serif;font-size:17.5px;line-height:29px}
.calendar{left:102px;top:598px;width:182px;height:188px;background:var(--panel);color:var(--white);box-shadow:0 1px 3px rgba(0,0,0,.4)}
.calendar h2{position:absolute;left:27px;top:8px;font-family:"Questrial",sans-serif;font-weight:400;font-size:25px}
.calendar .rule{position:absolute;left:0;top:22px;width:20px;height:1px;background:var(--white)}
.calendar ul{list-style:none;position:absolute;left:4px;top:49px;font-size:10.5px;line-height:26px}
.calendar li b{font-weight:400;display:inline-block;width:40px}
.calendar .btn{position:absolute;left:0;bottom:0;height:30px}
.calendar .label{width:145px}.calendar .arrow{width:37px;background:var(--btn-dark)}

.welcome-head{left:301px;top:422px;width:580px;display:flex;align-items:center;gap:8px}
.welcome-head h1{font-family:"Questrial",sans-serif;font-weight:400;font-size:21.5px;white-space:nowrap}
.welcome-head i{flex:1;height:1px;background:var(--ink)}
.welcome-body{left:301px;top:457px;width:582px;font-size:10.6px;line-height:12.4px;color:#333}
.welcome-body p+p.gap{margin-top:6px}
.divider{left:303px;top:674px;width:433px;height:1px;background:var(--ink)}
.welcome-btn{left:743px;top:658px}
.welcome-btn .label{width:98px;background:var(--btn-dark);color:var(--white)}
.welcome-btn .arrow{width:37px}

.ads-title{left:303px;top:683px;font-size:22px;line-height:22px;text-align:center;width:108px}
.ads-note{left:304px;top:739px;width:115px;font-size:7.8px;line-height:10px;text-transform:uppercase;color:#444}
.ad-banner{left:425px;top:718px;width:454px;height:52px;background:var(--banner);display:flex;align-items:center;justify-content:center;font-family:"Open Sans",sans-serif;font-weight:600;font-size:34px;color:var(--banner-ink);letter-spacing:-.5px}

.card{top:825px;width:248px;height:309px;background:var(--white);box-shadow:0 1px 3px rgba(0,0,0,.25)}
.card .photo{height:149px}
.card h3{position:absolute;left:20px;top:158px;font-family:"Questrial",sans-serif;font-weight:400;font-size:17px}
.card p{position:absolute;left:19px;top:190px;width:215px;font-size:10.3px;line-height:12.4px;color:#333}
.card .btn{position:absolute;left:0;bottom:0;width:248px}
.card .label{flex:1;background:var(--black);color:var(--white)}
.card .arrow{width:37px;background:var(--btn-dark)}
.card-a{left:102px}.card-b{left:367px}.card-c{left:631px}
.card-a .photo{background:linear-gradient(180deg,#c9c2a8,#5f6a52 55%,#24282c 80%,#8a8a86)}
.card-b .photo{background:linear-gradient(180deg,#8a7f74,#1b2a78 55%,#0f1746 80%,#6d6a66)}
.card-c .photo{background:linear-gradient(90deg,#8fa1b6,#c2cad3 50%,#c41f22 85%,#9e1416)}

.site-footer{left:0;top:1150px;width:993px;height:50px;background:var(--black);display:flex;justify-content:center;align-items:center;gap:17px;font-family:"Questrial",sans-serif;font-size:12.8px;color:var(--white);padding-left:14px}
</style>
</head>
<body>
<header class="site-header abs">
  <div class="brand abs"><span class="name">Ravelin Guild</span><span class="region">of new Zealand</span></div>
  <div class="social abs" aria-label="Social links"><span></span><span></span><span></span></div>
  <nav class="top-nav abs"><span>FORUM</span><span>GALLERY</span><span>EVENTS</span></nav>
</header>

<section class="hero abs">
  <div class="hero-photo abs" role="img" aria-label="Blue roadster with white racing stripes parked on a desert road"></div>
  <h2 class="hero-title abs head-font" style="font-weight:400">Ravelin Guild</h2>
  <p class="hero-text abs">Welcome to Ravelin Guild of New Zealand. We love Ravelin’s style At home On the Track or On Show. Share your interest about Ravelin's now and join our Club</p>
  <div class="btn hero-btn abs"><span class="label">Learn More</span><span class="arrow">&gt;</span></div>
</section>

<div class="slider-dots abs"><span class="on"></span><span></span><span></span><span></span></div>

<nav class="side-nav abs"><div>Home</div><div>Calendar</div><div>Membership</div><div>Advertisers</div><div>Contact Us</div></nav>

<aside class="calendar abs">
  <i class="rule"></i><h2>CALENDAR</h2>
  <ul>
    <li><b>15/12</b>Lorem Ipsum is simply...</li>
    <li><b>17/12</b>&nbsp;dummy text...</li>
    <li><b>19/12</b>Lorem Ipsum is simply...</li>
    <li><b>25/12</b>&nbsp;dummy text...</li>
  </ul>
  <div class="btn"><span class="label">Learn More</span><span class="arrow">&gt;</span></div>
</aside>

<div class="welcome-head abs"><h1>Welcome to Ravelin Guild</h1><i></i></div>
<div class="welcome-body abs">
  <p>This is not an official website related to the manufacture of Ravelin cars but it is a website devoted to all those that share a passion for the Ravelin.</p>
  <p>Welcome to our website. Our aim is to make this site user friendly and we have included a 'Forum' for the benefit of all Ravelin owners in New Zealand regardless of Ravelin kit type. Our intent for the Forum is to give those people interested/active in the Ravelin NZ scene a common vehicle to share ideas, problem solve and plan events.</p>
  <p>Our Calendar lists up-to-date and upcoming events. Check this regularly, especially for those last-minute runs that are often organised at very short notice upon the discovery of fine weather in Auckland!</p>
  <p class="gap">No matter where your taste lies, the Ravelin Motor Guild of New Zealand has members that fit all categories. From showing your prize possession off at a local car show or promotional event, to risking it all on the race track. If you’re into Ravelin’s then this is the place to be!</p>
  <p>The club regularly attends shows such as the Concours D’Elegance at Riverside Park, All Marques Day and fundraising events such as the Prostate Cancer Runs. Just for that adrenalin rush a few hot laps at Kowhai Downs or even Rally Kauri, to test your nerves!</p>
  <p>So if you’re into Ravelin’s, thinking of building one, looking for advice, or just need to be near one check out the Calendar pages or contact details</p>
</div>
<div class="divider abs"></div>
<div class="btn welcome-btn abs"><span class="label">Learn More</span><span class="arrow">&gt;</span></div>

<h2 class="ads-title abs head-font" style="font-weight:400">Advertising Banners</h2>
<p class="ads-note abs">Please support our advertisers who fund this site for the benefit of all</p>
<div class="ad-banner abs">northshore gearworks</div>

<article class="card card-a abs">
  <div class="photo" role="img" aria-label="Black roadster parked on a driveway in front of a house"></div>
  <h3>Fest no1</h3>
  <p>Lorem Ipsum is simply dummy text of the printing and typesetting industry. Lorem Ipsum has been the industry's standard dummy text ever since the 1500s, when an unknown printer took a galley of type and scrambled.</p>
  <div class="btn"><span class="label">Learn More</span><span class="arrow">&gt;</span></div>
</article>
<article class="card card-b abs">
  <div class="photo" role="img" aria-label="Dark blue roadster on display at a car show"></div>
  <h3>Fest no1</h3>
  <p>Lorem Ipsum is simply dummy text of the printing and typesetting industry. Lorem Ipsum has been the industry's standard dummy text ever since the 1500s, when an unknown printer took a galley of type and scrambled.</p>
  <div class="btn"><span class="label">Learn More</span><span class="arrow">&gt;</span></div>
</article>
<article class="card card-c abs">
  <div class="photo" role="img" aria-label="Row of silver and red roadsters lined up at a club meet"></div>
  <h3>Fest no3</h3>
  <p>Lorem Ipsum is simply dummy text of the printing and typesetting industry. Lorem Ipsum has been the industry's standard dummy text ever since the 1500s, when an unknown printer took a galley of type and scrambled.</p>
  <div class="btn"><span class="label">Learn More</span><span class="arrow">&gt;</span></div>
</article>

<footer class="site-footer abs">
  <span>HOME</span><span>CALENDAR</span><span>MEMBERSHIP</span><span>ADVERTISERS</span><span>CONTACT US</span><span>FORUM</span><span>GALLERY</span><span>EVENTS</span>
</footer>
</body>
</html>
```